Virtual Assistant/Online Marketing Business Card/Stationary

I need a professional but modern business card/stationary for my company in Dallas called BrivoLane. BrivoLane is a virtual assistant specializing in online marketing. I would like a unique design that stands out and makes my brand clear. Incorporating the logo is a must and have attached it to this brief.

Target Market(s)

small business owners & entrepreneurs, 35-65

Industry/Entity Type

Business

Contact Information for Business Card

Dorla Finch
dorlafinch@brivolane.biz
(214) 555-0187
brivolane.biz

Font styles to use
Sans Serif

Colors
f04a50
3176b5
9bcb3c

Requirements
Must have
• Colors that match the logo colors. Logo integration

```html
<!DOCTYPE html>
<html lang="en">
<head>
<meta charset="utf-8">
<title>BrivoLane Business Card</title>
<link rel="stylesheet" href="https://fonts.googleapis.com/css2?family=Montserrat:wght@500;700;800&display=swap">
<style>
  :root {
    --page: #ecebe8;
    --card: #ffffff;
    --ink: #231f1c;
    --tone-dark: #2a2622;
    --tone-red: #d23f24;
    --tone-teal: #0f9a9a;
    --shadow: rgba(0, 0, 0, 0.14);
  }
  * { box-sizing: border-box; margin: 0; padding: 0; }
  html, body {
    width: 1200px;
    height: 800px;
    overflow: hidden;
    background: var(--page);
    font-family: "Montserrat", Arial, sans-serif;
    color: var(--ink);
  }
  .sheet {
    width: 1200px;
    height: 800px;
    display: flex;
    align-items: center;
    justify-content: center;
    gap: 60px;
  }
  .card {
    position: relative;
    width: 500px;
    height: 286px;
    background: var(--card);
    box-shadow: 0 8px 24px var(--shadow);
    overflow: hidden;
  }
  .card-accent {
    position: absolute;
    left: 0;
    top: 0;
    width: 200px;
    height: 100%;
    background: linear-gradient(100deg, var(--tone-dark) 0%, var(--tone-red) 50%, var(--tone-teal) 100%);
  }

  .brand-name {
    position: absolute;
    left: 220px;
    top: 120px;
    width: 260px;
    text-align: center;
    font-weight: 800;
    font-size: 36px;
    line-height: 44px;
    letter-spacing: -0.5px;
    color: var(--ink);
  }

  .holder-name {
    position: absolute;
    left: 220px;
    top: 112px;
    width: 260px;
    text-align: center;
    font-weight: 700;
    font-size: 26px;
    line-height: 32px;
    letter-spacing: 0.5px;
    text-transform: uppercase;
    color: var(--ink);
  }
  .contact-list {
    position: absolute;
    left: 228px;
    top: 170px;
    width: 262px;
    display: grid;
    grid-template-columns: auto auto;
    column-gap: 14px;
    row-gap: 5px;
    list-style: none;
    font-weight: 500;
    font-size: 9.5px;
    color: var(--ink);
  }
  .contact-item {
    display: flex;
    align-items: center;
    gap: 5px;
    white-space: nowrap;
  }
  .contact-icon {
    width: 9px;
    height: 9px;
    fill: var(--ink);
    flex: none;
  }
</style>
</head>
<body>
<main class="sheet">

  <section class="card card-front" aria-label="Card front">
    <div class="card-accent" role="img" aria-label="Decorative sweep of dark, red and teal bands"></div>
    <p class="brand-name">BrivoLane</p>
  </section>

  <section class="card card-back" aria-label="Card back">
    <div class="card-accent" role="img" aria-label="Decorative sweep of dark, red and teal bands"></div>
    <h1 class="holder-name">Dorla Finch</h1>
    <ul class="contact-list">
      <li class="contact-item">
        <svg class="contact-icon" viewBox="0 0 10 10" aria-hidden="true"><path d="M1,3 Q5,0 9,3 L8,4.5 L6.5,3.8 L6.5,3 Q5,2.5 3.5,3 L3.5,3.8 L2,4.5 Z M2.5,5 L7.5,5 L8.5,9 L1.5,9 Z"/></svg>
        (214) 555-0187
      </li>
      <li class="contact-item">
        <svg class="contact-icon" viewBox="0 0 10 10" aria-hidden="true"><path d="M1,2 L9,2 L9,8 L1,8 Z M1.8,2.8 L5,5.4 L8.2,2.8 Z"/></svg>
        dorlafinch@brivolane.biz
      </li>
      <li class="contact-item">
        <svg class="contact-icon" viewBox="0 0 10 10" aria-hidden="true"><circle cx="5" cy="5" r="4.5"/><path d="M5,0.5 Q2.5,5 5,9.5 M5,0.5 Q7.5,5 5,9.5 M0.5,5 L9.5,5" stroke="#fff" stroke-width="0.7" fill="none"/></svg>
        brivolane.biz
      </li>
    </ul>
  </section>

</main>
</body>
</html>
```